Stylish Design With Simple UI For Appointment Site

ONE WEEK TO GO - STILL CONSIDERING NEW DESIGNS!

Note: Logo file now attached. Extra credit to anyone who offers basic HTML templates in the final deliverable, incorporating the individual components of the design (using DIVs and CSS).

There are two key requirements for this site:

1. It makes our site look like one of the most professional of its kind. We want to look the part;
2. It has a very simple, straight-forward user interface. We're nothing without being intuitive.

Our site will be used by other businesses to set up their own online booking systems.

Logo samples attached. The colour scheme is not yet set but two possible options are:

1. Dark (#323B3A) & Blue (#12B5D4) on White background
2. White & Yellow (#FEF102) on Grey (#3A3A3C) background

For inspiration, and an idea of what we like, take a look at quillpost.example - it's very clear and eye-catching, although its pages are longer than we would like ours to be. Oh but we don't need a chimp! Instead of the section with the chimp in, we would like a changing image headline section on the home page, in the style of bellvarine.example.co.uk (with a less high image; we have attached one image which you may want to try out with this, but happy to see other ideas).

Any graphics included must be royalty free and free for commercial use. Fonts should be readily available and specified.

We would like to see the design applied to the following pages:

1. The main public home page (features header, login prompt, menu, changing image banner with headlines, main body, footer menu).
2. A secondary public page (features a similar layout to home page but without image headline banner, includes extra panels/body detail).
3. The Control Panel page (features several list panels and an add appointment button).
4. A list-style administration page (with popup item editor window).
5. A settings administration page (with form).

In that order, a sample walk-through design spec will be attached.

To summarise, we are looking for someone to put forward not only a design but something which also focuses on the user interface. The designer should consider all of the examples and guidance given, but shouldn't let that limit any innovation.

Happy to respond to any questions and give constant feedback.

Thank you.

-*-*-*-*-*-*-*-*-*-*-*-*-*-*-*-*-

Update, 18th Nov 2011:

1. I'm about the upload the logos so you can incorporate these into your designs.

2. A UI question of mine is how to move from a list view (e.g. Resources) to editing one of those items in the list. In the spec document I showed a popup editor for these items but I don't know if that's the best thing to do. Happy to see other ideas on this - whatever the best user experience would be.

3. On the designs in the spec document I've not included any help functionality. It would be good to include pieces of guidance on each page of the administration area to help the user - guess these could either be info panels on the pages themselves or info popups. Again, would be good to see some ideas in the designs.

Also, just to be clear, I am really looking for something that looks like a modern innovative "web app" rather than it looking like a promotional corporate web site.

Target Market(s)

Owners of businesses of all types (e.g. salons, small hotels, surgeries, etc).

Industry/Entity Type

Commercial

Requirements
Must have
• Headline image transition panel on home page.

Layout, graphic and font styles along similar lines to quillpost.example, bellvarine.example.co.uk, etc.
Nice to have
• Blog feed panel on the home page.

Innovative ideas for improvements to the spec.
Should not have
• Anything which can't be practically rendered when the design is converted to HTML.

Should not be overly influenced by the layout and style in the attached spec - that should just be a guide to the content and layout of the site.

```html
<!DOCTYPE html>
<html lang="en">
<head>
<meta charset="utf-8">
<title>Tidebook – Online Booking</title>
<link rel="stylesheet" href="https://fonts.googleapis.com/css2?family=Arimo:wght@400;700&display=swap">
<style>
  :root{
    --ink:#323b3a;
    --brand-blue:#12b5d4;
    --heading-teal:#137a8a;
    --text:#222;
    --field:#4a4a4a;
    --frame:#5b5b5f;
    --panel:#e4e4e4;
    --tab-top:#fafafa;
    --tab-bottom:#d6d6d6;
    --footer-top:#e9e9e9;
    --footer-bottom:#fbfbfb;
    --header-wash:#d7eff5;
  }
  *{box-sizing:border-box;margin:0;padding:0}
  html,body{width:1200px;height:1127px;overflow:hidden}
  body{background:#fdfdfd;font-family:"Arimo",Arial,sans-serif;color:var(--text);position:relative}
  a{color:inherit}
  .abs{position:absolute}

  /* header */
  .header-wash{left:340px;top:0;width:760px;height:190px;background:radial-gradient(ellipse at 60% 30%,var(--header-wash) 0%,rgba(215,239,245,.5) 40%,rgba(253,253,253,0) 75%)}
  .brand{left:64px;top:72px;display:flex;align-items:center;gap:16px}
  .brand-square{width:44px;height:44px;background:var(--brand-blue)}
  .brand-name{font-size:42px;font-weight:400;letter-spacing:6px;color:var(--ink);line-height:44px}

  .login-label{right:260px;font-size:17px;color:#444}
  .login-field{left:955px;width:217px;height:43px;background:var(--field);border:1px solid #333;box-shadow:inset 0 2px 4px rgba(0,0,0,.5)}
  .forgot{left:971px;top:188px;font-size:14px;color:#333;text-decoration:underline}
  .login-btn{left:1099px;top:180px;width:73px;height:34px;background:linear-gradient(#6a7488,#46506a);border:1px solid #2e3446;color:#fff;font-size:17px;display:flex;align-items:center;justify-content:center}

  /* navigation */
  .main-nav{left:62px;top:220px;height:64px;display:flex;box-shadow:0 3px 6px rgba(0,0,0,.25)}
  .nav-tab{height:64px;display:flex;align-items:center;justify-content:center;font-size:20px;color:#111;text-decoration:none;background:linear-gradient(var(--tab-top),var(--tab-bottom));border-right:1px solid #bbb}
  .nav-tab.is-active{background:linear-gradient(#28bfdc,#0c93b3);color:#fff}
  .locale{left:955px;top:247px;display:flex;align-items:center;gap:8px;font-size:15px;color:#444}
  .locale-flag{width:18px;height:12px;background:#3a4a8c;border:1px solid #999}
  .locale-caret{width:0;height:0;border-left:6px solid transparent;border-right:6px solid transparent;border-top:7px solid #555;margin-left:6px}

  /* banner */
  .banner{left:29px;top:284px;width:1147px;height:377px;background:var(--frame);border-radius:0 0 8px 8px}
  .banner-stage{left:72px;top:293px;width:1063px;height:360px;background:#000;border-radius:0 0 8px 8px;overflow:hidden}
  .banner-photo{left:0;top:0;width:420px;height:360px;background:radial-gradient(ellipse at 20% 40%,#d8dadc 0%,#b5b8bb 45%,#4a4a4a 80%,#000 100%)}
  .banner-copy{left:517px;top:410px;width:560px;font-size:16px;line-height:32px;color:#e6e6e6}
  .signup-btn{left:880px;top:516px;width:146px;height:36px;border-radius:18px;background:linear-gradient(#fff,#c9c9c9);color:#111;font-size:19px;font-weight:700;display:flex;align-items:center;justify-content:center}
  .banner-dots{left:992px;top:621px;display:flex;gap:12px}
  .banner-dot{width:13px;height:13px;border-radius:50%;background:#9a9a9a}
  .banner-dot.is-current{background:#fff}
  .banner-arrow{top:456px;width:20px;height:32px}

  /* content */
  .info-panel{left:29px;top:690px;width:1147px;height:294px;background:var(--panel);border-radius:10px}
  .info-divider{left:598px;top:718px;width:1px;height:240px;background:linear-gradient(transparent,#c4c4c4,transparent)}
  .info-col{top:710px;width:505px}
  .info-title{font-size:29px;font-weight:400;color:var(--heading-teal);margin-bottom:20px}
  .info-text{font-size:14px;line-height:24px;color:#111}
  .view-more{font-size:15px;color:var(--heading-teal);text-decoration:underline;top:928px}

  /* footer */
  .site-footer{left:0;top:1003px;width:1200px;height:124px;border-top:4px solid #c9c9c9;background:linear-gradient(var(--footer-top),var(--footer-bottom))}
  .footer-links{left:32px;top:1032px;font-size:13px;color:#333;display:flex;gap:12px}
  .footer-links a{text-decoration:none}
  .copyright{left:32px;top:1064px;font-size:13px;color:#333}
  .connect{left:954px;top:1032px;font-size:13px;color:#333}
  .social{left:954px;top:1063px;display:flex;gap:22px}
  .social-square{width:26px;height:26px;background:#8a8f96;border-radius:2px}
</style>
</head>
<body>

<header>
  <div class="abs header-wash" role="img" aria-label="Soft light-blue decorative wave behind the login area"></div>

  <div class="abs brand">
    <span class="brand-square"></span>
    <span class="brand-name">TIDEBOOK</span>
  </div>

  <span class="abs login-label" style="top:70px">user name :</span>
  <div class="abs login-field" style="top:60px"></div>
  <span class="abs login-label" style="top:132px">Pass word :</span>
  <div class="abs login-field" style="top:121px"></div>
  <a class="abs forgot">forgot password?</a>
  <div class="abs login-btn">Log In</div>

  <nav class="abs main-nav">
    <a class="nav-tab is-active" style="width:123px">HOME</a>
    <a class="nav-tab" style="width:149px">FEATURES</a>
    <a class="nav-tab" style="width:152px">PRICING</a>
    <a class="nav-tab" style="width:187px;border-right:0">CONTACT US</a>
  </nav>

  <div class="abs locale">
    <span class="locale-flag"></span>
    <span>United States - English</span>
    <span class="locale-caret"></span>
  </div>
</header>

<section>
  <div class="abs banner"></div>
  <div class="abs banner-stage">
    <div class="abs banner-photo" role="img" aria-label="Close-up photograph of a clock face"></div>
  </div>
  <p class="abs banner-copy">Aurelian are also reproduced in their exact original form, accompanied by English versions from the 1914 translation by J. Morrow.</p>
  <div class="abs signup-btn">Sign Up</div>
  <div class="abs banner-dots">
    <span class="banner-dot is-current"></span><span class="banner-dot"></span><span class="banner-dot"></span><span class="banner-dot"></span><span class="banner-dot"></span>
  </div>
  <svg class="abs banner-arrow" style="left:37px" viewBox="0 0 20 32" aria-hidden="true"><path d="M16 2 L4 16 L16 30" fill="none" stroke="#222" stroke-width="3"/></svg>
  <svg class="abs banner-arrow" style="left:1149px" viewBox="0 0 20 32" aria-hidden="true"><path d="M4 2 L16 16 L4 30" fill="none" stroke="#222" stroke-width="3"/></svg>
</section>

<main>
  <div class="abs info-panel"></div>
  <div class="abs info-divider"></div>

  <article class="abs info-col" style="left:66px">
    <h2 class="info-title">Make Your Self Available</h2>
    <p class="info-text">The standard chunk of Lorem Ipsum used since the 1500s is reproduced below for those interested. Sections 1.10.32 and 1.10.33 from "de Finibus Bonorum et Malorum" by Aurelian are also reproduced in their exact original form, accompanied by English versions from the 1914 translation combined with a handful of model sentence structures, to generate Lorem Ipsum which looks reasonable. humour, or non-characteristic words etc.</p>
  </article>
  <a class="abs view-more" style="left:497px">View more</a>

  <article class="abs info-col" style="left:631px">
    <h2 class="info-title">What’s Happening?</h2>
    <p class="info-text">The standard chunk of Lorem Ipsum used since the 1500s is reproduced below for those interested. Sections 1.10.32 and 1.10.33 from "de Finibus Bonorum et Malorum" by Aurelian are also reproduced in their exact original form, accompanied by English versions from the 1914 translation combined with a handful of model sentence structures, to generate Lorem Ipsum which looks reasonable. humour, or non-characteristic words etc.</p>
  </article>
  <a class="abs view-more" style="left:1062px">View more</a>
</main>

<footer>
  <div class="abs site-footer"></div>
  <nav class="abs footer-links">
    <a>Home</a><span>|</span><a>Features</a><span>|</span><a>Pricing</a><span>|</span><a>Contact US</a><span>|</span><a>Sitemap</a>
  </nav>
  <p class="abs copyright">Copyright © 2011 www.tidebook.example&nbsp; All rights reserved</p>
  <p class="abs connect">Connect with us :</p>
  <div class="abs social">
    <span class="social-square"></span><span class="social-square"></span><span class="social-square"></span><span class="social-square"></span><span class="social-square"></span>
  </div>
</footer>

</body>
</html>
```